KVT Roofing Pty Ltd

We are a high end residential Roofing company
We would like something silimar to the attached logo with the same color scheme

Target Market(s)

High end residential Builders & Architects

Industry/Entity Type

Residential

```html
<!DOCTYPE html>
<html lang="en">
<head>
<meta charset="utf-8">
<title>KVT Roofing Pty Ltd – Business Card</title>
<link href="https://fonts.googleapis.com/css2?family=Montserrat:wght@400;600;700&display=swap" rel="stylesheet">
<style>
  :root {
    --page-bg: #e9ebed;
    --slate-light: #8d9ca6;
    --slate-dark: #3a4853;
    --card-white: #ffffff;
    --sky-blue: #1e9ad6;
    --accent-cyan: #3fb6e3;
    --ink-grey: #5d6770;
    --ink-dark: #3c4650;
  }
  * { box-sizing: border-box; margin: 0; padding: 0; }
  html, body {
    width: 1200px;
    height: 913px;
    overflow: hidden;
    background: var(--page-bg);
    font-family: "Montserrat", Arial, sans-serif;
  }
  .canvas {
    position: relative;
    width: 1200px;
    height: 913px;
    display: flex;
    align-items: center;
    justify-content: center;
    gap: 60px;
  }
  .card {
    position: relative;
    width: 520px;
    height: 318px;
    border-radius: 4px;
    box-shadow: 0 10px 28px rgba(40, 50, 60, 0.22);
    overflow: hidden;
  }

  /* Front */
  .card-front {
    background: linear-gradient(170deg, var(--slate-light) 0%, #5f6f7b 45%, var(--slate-dark) 100%);
    display: flex;
    align-items: center;
    justify-content: center;
  }
  .brand-front {
    display: flex;
    align-items: center;
    gap: 16px;
  }
  .brand-mark {
    width: 26px;
    height: 26px;
    background: var(--accent-cyan);
  }
  .brand-front .brand-name {
    color: #ffffff;
    font-weight: 700;
    font-size: 40px;
    letter-spacing: 3px;
    text-transform: uppercase;
  }

  /* Back */
  .card-back {
    background: var(--card-white);
    padding: 34px 36px;
  }
  .brand-back {
    position: absolute;
    left: 150px;
    top: 64px;
    display: flex;
    align-items: center;
    gap: 12px;
  }
  .brand-back .brand-name {
    color: var(--ink-grey);
    font-weight: 700;
    font-size: 28px;
    letter-spacing: 2px;
    text-transform: uppercase;
  }
  .brand-back .brand-mark { width: 18px; height: 18px; }
  .address {
    position: absolute;
    right: 36px;
    top: 40px;
    text-align: right;
    font-weight: 700;
    font-size: 11px;
    line-height: 1.45;
    color: var(--ink-grey);
    text-transform: uppercase;
    letter-spacing: 0.5px;
  }
  .contact {
    position: absolute;
    left: 36px;
    bottom: 34px;
  }
  .person-name {
    color: var(--sky-blue);
    font-weight: 700;
    font-size: 17px;
    text-transform: uppercase;
    letter-spacing: 0.5px;
  }
  .person-role {
    color: var(--ink-grey);
    font-size: 11px;
    text-transform: uppercase;
    letter-spacing: 1px;
    margin-top: 1px;
  }
  .phone {
    color: var(--sky-blue);
    font-weight: 700;
    font-size: 18px;
    margin-top: 18px;
    letter-spacing: 0.5px;
  }
  .email {
    color: var(--ink-dark);
    font-size: 11px;
    text-transform: uppercase;
    letter-spacing: 0.6px;
    margin-top: 18px;
  }
</style>
</head>
<body>
  <main class="canvas">
    <section class="card card-front" aria-label="Card front">
      <div class="brand-front">
        <span class="brand-mark"></span>
        <span class="brand-name">KVT Roofing</span>
      </div>
    </section>

    <section class="card card-back" aria-label="Card back">
      <div class="brand-back">
        <span class="brand-mark"></span>
        <span class="brand-name">KVT Roofing</span>
      </div>
      <address class="address">118 Harlow Street,<br>Bayside North</address>
      <div class="contact">
        <p class="person-name">Corran Whitfield</p>
        <p class="person-role">General Manager</p>
        <p class="phone">0400 555 218</p>
        <p class="email">cwhitfield@kvtroofing.com.au</p>
      </div>
    </section>
  </main>
</body>
</html>
```